CloudRiver Business Card

I need something that flows with the logo and looks professional but creative. I included the thumbnail file of the photo but will upload the source file once I have it. Colors of business card should flow. I am interested in doing the translucent clear plastic cards as well. My company is called CloudRiver in one word and the contact details are below:

Dale Hollings
555-318-4720
www.CloudRiverTx.example
dhollings_47@mailbox.example
Updates

Too much red. I'd rather focus on the blue and put some silver or grey in there.

New Files uploaded. Like the designs so far and am looking forward to seeing more.

Looking for a whole new direction. Let's forget about the plastic card. Let's focus on the blue more than red. I still haven't seen something that really grabs me.

Industry/Entity Type

Plastic

```html
<!DOCTYPE html>
<html lang="en">
<head>
<meta charset="utf-8">
<title>CloudRiver Business Card</title>
<link href="https://fonts.googleapis.com/css2?family=Alegreya+Sans+SC:wght@400&family=PT+Sans:wght@700&display=swap" rel="stylesheet">
<style>
  :root {
    --page-bg: #eceae6;
    --card-dark: #232526;
    --card-light: #fbfbfb;
    --accent-red: #d9252c;
    --accent-red-dark: #b01a20;
    --brand-blue: #1f8fd0;
    --text-blue: #1c66aa;
    --wave-blue: rgba(29, 79, 122, 0.45);
    --wave-fade: rgba(29, 79, 122, 0);
  }
  * { margin: 0; padding: 0; box-sizing: border-box; }
  html, body { width: 1200px; height: 1000px; overflow: hidden; }
  body {
    background: var(--page-bg);
    position: relative;
    font-family: "PT Sans", sans-serif;
  }
  .card {
    position: absolute;
    left: 320px;
    width: 560px;
    height: 320px;
    overflow: hidden;
    box-shadow: 0 6px 18px rgba(0,0,0,0.18);
  }
  .card--back { top: 110px; background: var(--card-light); }
  .card--front { top: 560px; background: var(--card-dark); }

  .back-side-band {
    position: absolute; left: 0; top: 0; width: 16px; height: 100%;
    background: linear-gradient(90deg, var(--accent-red-dark), var(--accent-red));
  }
  .back-bottom-band {
    position: absolute; left: 0; bottom: 0; width: 100%; height: 22px;
    background: linear-gradient(180deg, var(--accent-red), var(--accent-red-dark));
  }
  .contact {
    position: absolute; left: 48px; top: 34px;
    font-family: "Alegreya Sans SC", sans-serif;
    color: var(--text-blue);
    font-size: 21px;
    line-height: 31px;
    list-style: none;
  }
  .back-brand {
    position: absolute; right: 34px; bottom: 46px;
    font-family: "PT Sans", sans-serif; font-weight: 700;
    font-size: 38px; line-height: 1; color: var(--brand-blue);
  }
  .front-wave-area {
    position: absolute; left: 0; top: 0; width: 240px; height: 100%;
    background: radial-gradient(ellipse 60% 80% at 45% 50%, var(--wave-blue), var(--wave-fade) 75%);
  }
  .front-brand {
    position: absolute; left: 150px; top: 118px;
    font-family: "PT Sans", sans-serif; font-weight: 700;
    font-size: 66px; line-height: 1; color: var(--brand-blue);
  }
</style>
</head>
<body>
  <section class="card card--back" aria-label="Business card back">
    <div class="back-side-band"></div>
    <ul class="contact">
      <li>Dale Hollings</li>
      <li>555-318-4720</li>
      <li>www.CloudRiverTx.example</li>
      <li>dhollings_47@mailbox.example</li>
    </ul>
    <div class="back-brand">CloudRiver</div>
    <div class="back-bottom-band"></div>
  </section>

  <section class="card card--front" aria-label="Business card front">
    <div class="front-wave-area" role="img" aria-label="Decorative flowing blue wave lines"></div>
    <div class="front-brand">CloudRiver</div>
  </section>
</body>
</html>
```